Flyer-Design für Anbieter von hochwertigem Futter für Kaninchen
Zielgruppe
Wir bieten hochwertiges Futter (Hauptfutter wie Heu aus eigener Herstellung aber auch Zusatzfutter) für Kaninchen.
Unsere Zielgruppe sind laut Auswertung unsers Online-Shops hauptsächlich weibliche Kunden (82%) und im Durchschnitt 40 Jahre alt.
Aufgabenstellung
Allgemeines:
- Flyer soll als Werbemedium gestaltet werden
- Design im Querformat DinA5
Inhalte:
- Logo Grasbündel.de
- www. grasbündel.de
- Kunden bewerten mit 'sehr gut'
- Familienbetrieb seit über 100 Jahren
- Geprüftes Qualitätsheu aus der Eifel
- frischer, aromatischer Heuduft von naturbelassenen, grünen Eifelwiesen
- Heu, Stroh und viele weitere Produkte im Shop
- Ökologische Papier-Verpackung
- Schneller und kostengünstiger Versand
Zusatzinfos:
- Die Datei normalheupng.png kann als Logo verwendet werden
- Als Idee könnte evt. auch ein Bild 89328394.jpg (Eifellandschaft Heuernte) in irgendweiner Form integriert werden.
- Folgende Bilddateien wurden über Bildaro gekauft:
- Es können bei Bedarf auch Kosten für weitere Bilder erworben werden

```html
<!DOCTYPE html>
<html lang="de">
<head>
<meta charset="utf-8">
<title>Grasbündel Flyer</title>
<link rel="stylesheet" href="https://fonts.googleapis.com/css2?family=Arimo:wght@400;700&display=swap">
<style>
  :root {
    --stage: #cccccc;
    --paper: #f7f4a8;
    --ink: #333333;
    --gold-light: #fdd52a;
    --gold-deep: #fea500;
    --white: #ffffff;
  }
  html, body {
    margin: 0;
    padding: 0;
    width: 1200px;
    height: 1200px;
    overflow: hidden;
    background: var(--stage);
    font-family: "Arimo", Arial, sans-serif;
  }
  .flyer {
    position: absolute;
    left: 224px;
    top: 334px;
    width: 752px;
    height: 531px;
    background: var(--paper);
    overflow: hidden;
    color: var(--ink);
  }
  .flyer-shapes {
    position: absolute;
    inset: 0;
    width: 752px;
    height: 531px;
  }
  .brand-name {
    position: absolute;
    left: 244px;
    top: 182px;
    width: 130px;
    text-align: center;
    font-size: 22px;
    font-weight: 700;
    color: var(--ink);
  }
  .address {
    position: absolute;
    left: 61px;
    top: 183px;
    margin: 0;
    font-style: normal;
    font-size: 18.5px;
    line-height: 20.8px;
  }
  .address strong { font-weight: 700; }
  .benefits {
    position: absolute;
    left: 32px;
    top: 284px;
    margin: 0;
    padding: 0;
    list-style: none;
    font-size: 15.5px;
    line-height: 17.9px;
  }
  .benefits li {
    position: relative;
    padding-left: 29px;
  }
  .benefits .tick {
    position: absolute;
    left: 0;
    top: 2px;
    width: 14px;
    height: 14px;
  }
  .contact-lines {
    position: absolute;
    left: 25px;
    top: 485px;
    font-size: 14px;
    line-height: 16.5px;
    color: var(--white);
  }
  .phone {
    position: absolute;
    left: 202px;
    top: 490px;
    font-size: 26px;
    font-weight: 700;
    color: var(--white);
    letter-spacing: 0.3px;
  }
</style>
</head>
<body>
<div class="flyer">
  <svg class="flyer-shapes" viewBox="0 0 1210 855" preserveAspectRatio="none">
    <defs>
      <linearGradient id="goldTile" x1="0" y1="0" x2="1" y2="0">
        <stop offset="0" stop-color="#fdd52a"/>
        <stop offset="1" stop-color="#fea500"/>
      </linearGradient>
      <linearGradient id="contactBand" x1="0" y1="0" x2="1" y2="0">
        <stop offset="0" stop-color="#fea500"/>
        <stop offset="1" stop-color="#fdd52a"/>
      </linearGradient>
      <linearGradient id="fieldPhoto" x1="0" y1="0" x2="0" y2="1">
        <stop offset="0" stop-color="#c9c59a"/>
        <stop offset="0.25" stop-color="#6f8a3a"/>
        <stop offset="0.5" stop-color="#a9a748"/>
        <stop offset="1" stop-color="#8c9a3e"/>
      </linearGradient>
      <linearGradient id="bunnyPhoto" x1="0" y1="0" x2="1" y2="1">
        <stop offset="0" stop-color="#f2ece4"/>
        <stop offset="1" stop-color="#7d7166"/>
      </linearGradient>
      <linearGradient id="carrotPhoto" x1="0" y1="0" x2="0" y2="1">
        <stop offset="0" stop-color="#c6a47a"/>
        <stop offset="1" stop-color="#e9783a"/>
      </linearGradient>
    </defs>
    <polygon role="img" aria-label="Landschaftsfoto: Wiesen der Eifel mit Heuballen" fill="url(#fieldPhoto)"
      points="714,252 1027,565 1210,387 1210,122 1089,0 961,0"/>
    <polygon fill="#f0b000" opacity="0.55" points="950,252 1122,77 1210,165 1210,390 1040,560 950,470"/>
    <polygon role="img" aria-label="Nahaufnahme von Heuhalmen" fill="#a8aa9c"
      points="599,370 704,265 809,370 704,475"/>
    <polygon fill="url(#goldTile)" points="751,455 824,382 897,455 824,528"/>
    <polygon fill="url(#goldTile)" points="674,657 799,530 926,657 799,784"/>
    <polygon role="img" aria-label="Foto: Kaninchen mit Möhren" fill="url(#carrotPhoto)"
      points="1054,592 1210,452 1210,747"/>
    <polygon fill="#f39a1e" points="1108,512 1210,410 1210,432 1119,522"/>
    <polygon role="img" aria-label="Foto: Kaninchen auf der Wiese" fill="url(#bunnyPhoto)"
      points="1044,602 1170,728 1044,855 919,728"/>
    <polygon fill="#f4a81c" opacity="0.8" points="897,728 980,645 1062,728 980,811"/>
    <polygon class="contact-band" fill="url(#contactBand)" points="0,762 539,762 632,855 0,855"/>
  </svg>

  <div class="brand-name">Grasbündel</div>

  <address class="address">
    Grasbuendel.de<br>
    <strong>K. BRANDAU</strong><br>
    Lindenweg 12<br>
    54321 Talheim
  </address>

  <ul class="benefits">
    <li><svg class="tick" viewBox="0 0 14 14"><path d="M0.5 7 L5 13 L13.5 0.5 L5 9.5 Z" fill="#333"/></svg>Geprüftes Qualitätsheu aus der Eifel – Familienbetrieb<br>seit über 100 Jahren</li>
    <li><svg class="tick" viewBox="0 0 14 14"><path d="M0.5 7 L5 13 L13.5 0.5 L5 9.5 Z" fill="#333"/></svg>frischer, aromatischer Heuduft von naturbelassenen,<br>grünen Eifelwiesen</li>
    <li><svg class="tick" viewBox="0 0 14 14"><path d="M0.5 7 L5 13 L13.5 0.5 L5 9.5 Z" fill="#333"/></svg>Heu, Stroh und viele weitere Produkte<br>im Shop</li>
    <li><svg class="tick" viewBox="0 0 14 14"><path d="M0.5 7 L5 13 L13.5 0.5 L5 9.5 Z" fill="#333"/></svg>Kunden bewerten mit „sehr gut“</li>
    <li><svg class="tick" viewBox="0 0 14 14"><path d="M0.5 7 L5 13 L13.5 0.5 L5 9.5 Z" fill="#333"/></svg>Ökologische Papier-Verpackung</li>
    <li><svg class="tick" viewBox="0 0 14 14"><path d="M0.5 7 L5 13 L13.5 0.5 L5 9.5 Z" fill="#333"/></svg>Schneller und kostengünstiger Versand</li>
  </ul>

  <div class="contact-lines">
    mail@grasbuendel.de<br>
    www.grasbündel.de
  </div>
  <div class="phone">02345-6789</div>
</div>
</body>
</html>
```